I am medical doctor in surgery specialized in Urology and anti-aging. I need Web and Instagram design for a head cream , face cream and body lotion. I did a 2% GHK-Cu solution (head-face-body) with an professional pharmacist specialized in manufacturing creams. . GHK-Cu is a tri-peptide with solid scientific background to rejuvenate the skin (will stimulate collagen production) and can promote hair regrowth. Statistically 70% of peptides bought are fake on the market, I can personally guarantee about purity (my peptides are certified pure above 99% checked in an independent laboratory in London -UK.
I want to use the name 'Lunavel'. I secured already the domain names. I had an design for another project I could re-use for this project. The ribbon should include more blue. The font of Lunavel can be changed. I got a logo which is ok for me. Web design best coded with Wordpress.

Target Market(s)

Anti aging, skin care, hair regrowth, skin collagen

Industry/Entity Type

the cream can also be used after surgery for faster and better wound healing

Number of Pages Required

5+ page

Font styles to use
Sans Serif

Colors
0054AA
0677BA
7BADD7
CADEEF
E8F1F8

Requirements
Must have
• target population 30-70 years
Nice to have
• scientific proof, pictures before-after
Should not have
• GHK-Cu has solid scientific animal studies of anti-cancer properties. It is 100% safe for dermal human use.

```html
<!DOCTYPE html>
<html lang="en">
<head>
<meta charset="utf-8">
<title>About Lunavel</title>
<link href="https://fonts.googleapis.com/css2?family=Montserrat:wght@500;600;700&family=Nunito+Sans:wght@400;600&display=swap" rel="stylesheet">
<style>
:root{
  --blue-deep:#0054AA;
  --blue:#0677BA;
  --blue-soft:#7BADD7;
  --blue-pale:#CADEEF;
  --blue-mist:#E8F1F8;
  --ink:#1B2A3D;
  --text:#2F3B4C;
  --muted:#6B7A90;
  --line:#D7E3EF;
  --footer:#18273A;
  --white:#FFFFFF;
}
*{margin:0;padding:0;box-sizing:border-box}
html,body{width:1200px;height:2391px;overflow:hidden}
body{font-family:"Nunito Sans",sans-serif;color:var(--text);background:var(--white)}
.container{width:1025px;margin:0 auto;position:relative}
h1,h2,h3,.brand,.nav-link,.btn{font-family:"Montserrat",sans-serif}

.topbar{height:37px;background:linear-gradient(90deg,var(--blue-deep),var(--blue));color:var(--white);font:600 12px/37px "Montserrat",sans-serif;text-align:center}

.site-header{height:88px;border-bottom:1px solid var(--line);background:var(--white)}
.site-header .container{height:100%;display:flex;align-items:center}
.brand{display:flex;align-items:center;gap:8px;font-weight:700;font-size:20px;color:var(--blue);letter-spacing:.5px}
.brand-dot{width:14px;height:14px;border-radius:50%;background:var(--blue-soft)}
.nav{display:flex;gap:29px;margin-left:108px}
.nav-link{font-size:13px;font-weight:500;letter-spacing:1.4px;color:var(--ink);text-decoration:none;padding:6px 0}
.nav-link.active{color:var(--blue-deep);border-bottom:2px solid var(--blue-deep)}
.btn{margin-left:auto;width:151px;height:45px;border-radius:6px;background:var(--blue-deep);color:var(--white);font-size:13px;font-weight:700;letter-spacing:1.4px;display:flex;align-items:center;justify-content:center;text-decoration:none}

.hero{height:194px;background:linear-gradient(100deg,var(--blue-mist),var(--blue-pale));text-align:center;padding-top:54px}
.hero h1{font-size:37px;font-weight:700;color:var(--ink)}
.hero p{margin-top:18px;font-size:16px;color:var(--muted)}

.story{height:549px;padding-top:72px}
.story .container{display:flex;justify-content:space-between}
.story-text{width:490px}
.badge{display:inline-block;background:var(--blue-mist);color:var(--blue-deep);font:600 12px/33px "Montserrat",sans-serif;padding:0 15px;border-radius:17px}
.story h2{font-size:32px;font-weight:700;color:var(--ink);margin:22px 0 20px}
.story p{font-size:14px;line-height:24.5px;color:var(--muted);margin-bottom:17px}
.story p.lead{color:var(--text)}
.expertise{width:486px;height:349px;margin-top:29px;background:var(--blue-mist);border-radius:8px;text-align:center;padding-top:43px}
.expertise-icon{width:107px;height:107px;border-radius:50%;background:var(--blue);margin:0 auto;display:flex;align-items:center;justify-content:center}
.expertise h3{font-size:22px;font-weight:600;color:var(--ink);margin:23px 0 10px}
.expertise .sub{font-size:14px;color:var(--muted)}
.expertise .note{font-size:12.5px;line-height:21px;color:var(--muted);width:260px;margin:20px auto 0}

.commitment{height:703px;background:var(--blue-mist);padding-top:73px;text-align:center}
.section-title{font-size:32px;font-weight:700;color:var(--ink)}
.section-sub{font-size:16px;color:var(--muted);margin-top:16px}
.pillars{display:grid;grid-template-columns:repeat(3,322px);gap:29px 29px;justify-content:space-between;margin-top:46px;text-align:left}
.pillar{height:203px;background:var(--white);border:1px solid var(--line);border-radius:8px;padding:29px 29px 0}
.pillar-num{display:inline-block;width:38px;height:28px;border-radius:14px;background:var(--blue-mist);color:var(--blue-deep);font:700 11px/28px "Montserrat",sans-serif;text-align:center}
.pillar h3{font-size:19px;font-weight:600;color:var(--ink);margin:12px 0 14px}
.pillar p{font-size:13px;line-height:22.5px;color:var(--muted)}

.guarantee{height:432px;padding-top:75px;text-align:center}
.guarantee .section-sub{width:560px;margin:20px auto 0;line-height:28px}
.quote-box{width:622px;height:135px;margin:46px auto 0;background:var(--blue-mist);border-radius:8px;padding-top:36px}
.quote-box blockquote{font:600 19px "Montserrat",sans-serif;color:var(--blue-deep)}
.quote-box p{margin-top:16px;font-size:14px;color:var(--muted)}

.site-footer{height:388px;background:var(--footer);color:#C9D4E2;padding-top:55px}
.footer-grid{display:flex;height:268px}
.footer-about{width:402px}
.footer-about .brand{color:var(--blue-soft)}
.footer-about p{font-size:12.5px;line-height:22.5px;margin-top:30px;width:290px}
.footer-col{width:219px}
.footer-col h3{font-size:15px;font-weight:600;color:var(--white);margin-top:8px;margin-bottom:19px}
.footer-col a{display:block;font-size:12.5px;color:#C9D4E2;text-decoration:none;margin-bottom:14px}
.footer-bottom{border-top:1px solid #2C3C52;display:flex;justify-content:space-between;padding-top:27px;font-size:11.5px}
.footer-bottom nav{display:flex;gap:21px}
.footer-bottom nav a{color:#7F8EA3;text-decoration:none}
</style>
</head>
<body>
<div class="topbar">Clinically proven GHK-Cu • 99%+ purity certified • Trusted by surgeons worldwide</div>

<header class="site-header">
  <div class="container">
    <a class="brand"><span class="brand-dot"></span>LUNAVEL</a>
    <nav class="nav">
      <a class="nav-link">HOME</a>
      <a class="nav-link">PRODUCTS</a>
      <a class="nav-link">SCIENCE</a>
      <a class="nav-link">RESULTS</a>
      <a class="nav-link active">ABOUT</a>
      <a class="nav-link">CONTACT</a>
    </nav>
    <a class="btn">SHOP NOW</a>
  </div>
</header>

<section class="hero">
  <h1>About Lunavel</h1>
  <p>A surgeon’s commitment to purity, quality, and skin health.</p>
</section>

<section class="story">
  <div class="container">
    <div class="story-text">
      <span class="badge">★ Board-Certified Surgeon</span>
      <h2>My Story</h2>
      <p class="lead">As a medical doctor specializing in Urology and Anti-Aging Medicine, I have spent years studying the science of tissue repair and regeneration. GHK-Cu has always stood out to me as one of the most promising compounds for skin health and rejuvenation.</p>
      <p>However, I discovered that an alarming 70% of peptides sold on the market are fake or impure. This was unacceptable. I partnered with a professional pharmacist to create Lunavel — a line of GHK-Cu formulations that meet the rigorous standards I demand as a surgeon.</p>
      <p>Every batch is independently tested at a certified laboratory in London, UK, guaranteeing purity above 99%. This is my personal guarantee to you.</p>
    </div>
    <div class="expertise">
      <div class="expertise-icon">
        <svg width="30" height="30" viewBox="0 0 30 30" aria-hidden="true"><path d="M11 2h8v9h9v8h-9v9h-8v-9H2v-8h9z" fill="#fff"/></svg>
      </div>
      <h3>Medical Expertise</h3>
      <p class="sub">Specialized in Urology &amp; Anti-Aging Medicine</p>
      <p class="note">Partnered with a professional pharmacist for pharmaceutical-grade manufacturing and quality control.</p>
    </div>
  </div>
</section>

<section class="commitment">
  <div class="container">
    <h2 class="section-title">Our Commitment</h2>
    <p class="section-sub">Six pillars that define everything we do at Lunavel.</p>
    <div class="pillars">
      <article class="pillar"><span class="pillar-num">01</span><h3>Uncompromising Purity</h3><p>Every batch independently tested in London. 99%+ purity guaranteed with certificates available on request.</p></article>
      <article class="pillar"><span class="pillar-num">02</span><h3>Scientific Rigor</h3><p>Formulations based on peer-reviewed research with over 2,000 published studies on GHK-Cu.</p></article>
      <article class="pillar"><span class="pillar-num">03</span><h3>Medical Oversight</h3><p>Developed and supervised by a board-certified surgeon with deep expertise in anti-aging medicine.</p></article>
      <article class="pillar"><span class="pillar-num">04</span><h3>Proven Results</h3><p>Visible improvements in skin firmness, texture, and hair density within weeks of regular use.</p></article>
      <article class="pillar"><span class="pillar-num">05</span><h3>Safe for All</h3><p>100% safe for dermal human use. Gentle formulas made for daily care of scalp, face and body.</p></article>
      <article class="pillar"><span class="pillar-num">06</span><h3>Post-Surgery Trust</h3><p>Clinically proven to accelerate wound healing and reduce scarring after surgical procedures.</p></article>
    </div>
  </div>
</section>

<section class="guarantee">
  <h2 class="section-title">The Lunavel Guarantee</h2>
  <p class="section-sub">I personally stand behind every product we sell. If you are not satisfied, I will make it right.</p>
  <div class="quote-box">
    <blockquote>“Purity is not just a promise — it is a practice.”</blockquote>
    <p>Request your batch certificate of analysis at any time.</p>
  </div>
</section>

<footer class="site-footer">
  <div class="container">
    <div class="footer-grid">
      <div class="footer-about">
        <a class="brand"><span class="brand-dot"></span>LUNAVEL</a>
        <p>Advanced GHK-Cu formulations developed by a board-certified surgeon. Scientifically proven to rejuvenate skin, stimulate collagen, and promote hair regrowth. Every batch independently tested for purity above 99%.</p>
      </div>
      <div class="footer-col">
        <h3>Quick Links</h3>
        <a>Home</a><a>Products</a><a>About Us</a><a>The Science</a><a>Results</a><a>Contact</a>
      </div>
      <div class="footer-col">
        <h3>Products</h3>
        <a>Head Cream</a><a>Face Cream</a><a>Body Lotion</a>
      </div>
      <div class="footer-col">
        <h3>Contact</h3>
        <a>info@lunavel-care.com</a><a>Get in Touch</a><a>FAQ</a>
      </div>
    </div>
    <div class="footer-bottom">
      <span>© 2026 Lunavel. All rights reserved.</span>
      <nav><a>Privacy Policy</a><a>Terms of Service</a></nav>
    </div>
  </div>
</footer>
</body>
</html>
```